New Software Development Firm Needs Business Cards!

We just completed a successful logo design project on MakerHive and need to develop a business card design using that shiny new logo. We want a clean, modern design that communicates professionalism and tech savvy without being cliche'.

The company is "Bramble Logic, LLC", but our dba is "Bramble" The business card address should reflect the full company name in the address. The logo just uses "Bramble".

Photoshop or Illustrator source files will be required, along with exact font name(s) and source(s) used.

The design will need to work well with our letterhead as well. I'm also launching a project right now for letterhead and envelopes as well. Please submit to both projects! We're excited to see the designs. Thanks...

Target Market(s)

Small to medium business professionals

Industry/Entity Type

Business

Requirements
Must have
• Need place for:
- Company name and address (5 lines)
- Phone: (1 number)
- Fax: (1 number)
- Employee's name
- Employee's position
- Employee's email address
- Company web site URL
Nice to have
• Probably want a white card, but we're open to options.

```html
<!DOCTYPE html>
<html lang="en">
<head>
<meta charset="utf-8">
<title>Bramble Stationery</title>
<link rel="stylesheet" href="https://fonts.googleapis.com/css2?family=Open+Sans:wght@400;600&family=Arimo:wght@400&display=swap">
<style>
  :root {
    --ink: #111111;
    --black: #0d0d0d;
    --red: #e0232b;
    --paper: #ffffff;
    --grey-text: #333333;
    --light-text: #dddddd;
    --backdrop: #d9d9d9;
  }
  * { box-sizing: border-box; margin: 0; padding: 0; }
  html, body { width: 1200px; height: 900px; overflow: hidden; }
  body { background: var(--backdrop); position: relative; font-family: "Open Sans", sans-serif; color: var(--ink); }

  .icon-defs { position: absolute; width: 0; height: 0; }

  .brand { font-family: "Open Sans", sans-serif; font-weight: 400; letter-spacing: 0.5px; white-space: nowrap; line-height: 1; }

  .contact-list { list-style: none; white-space: nowrap; }
  .contact-list li { display: flex; align-items: center; gap: 6px; }
  .contact-list svg { width: 8px; height: 8px; fill: var(--red); flex: none; }

  /* Letterhead */
  .letterhead { position: absolute; left: 70px; top: 82px; width: 520px; height: 736px; background: var(--paper); display: flex; flex-direction: column; box-shadow: 0 2px 6px rgba(0,0,0,.15); }
  .letterhead-header { height: 150px; background: var(--black); border-bottom: 3px solid var(--red); display: flex; align-items: center; padding: 0 28px 0 32px; gap: 18px; }
  .letterhead-header .brand { color: var(--paper); font-size: 36px; }
  .company-block { border-left: 2px solid var(--red); padding-left: 10px; font-size: 8.5px; line-height: 13px; color: var(--light-text); white-space: nowrap; }
  .company-name { color: var(--red); font-size: 10px; }
  .letterhead-header .contact-list { font-size: 8.5px; line-height: 13px; color: var(--light-text); margin-left: auto; }
  .letter-body { flex: 1; padding: 26px 42px 0; font-family: "Arimo", sans-serif; font-size: 9.5px; line-height: 13.5px; color: var(--grey-text); }
  .letter-body p { text-align: justify; margin-bottom: 12px; }
  .greeting { margin-bottom: 12px; }
  .sign-off { margin-top: 16px; }
  .signature-row { display: flex; align-items: flex-end; gap: 12px; margin-top: 6px; }
  .signature { width: 150px; height: 46px; background: linear-gradient(90deg, #f4f4f4, #e9e9e9); }
  .signer { line-height: 13px; }
  .letterhead-footer { height: 12px; background: var(--black); border-top: 3px solid var(--red); }

  /* Business cards */
  .card { position: absolute; width: 420px; height: 240px; box-shadow: 0 2px 6px rgba(0,0,0,.2); }
  .card-back { left: 700px; top: 150px; background: var(--black); display: flex; flex-direction: column; align-items: center; justify-content: center; gap: 26px; }
  .card-back .brand { color: var(--paper); font-size: 44px; }
  .card-back .card-url { color: var(--light-text); font-size: 8px; letter-spacing: 3px; }

  .card-front { left: 700px; top: 450px; background: var(--paper); display: flex; flex-direction: column; }
  .card-front-main { flex: 1; padding: 30px 30px 0; display: grid; grid-template-columns: 1fr 1fr; grid-template-rows: auto 1fr; column-gap: 16px; }
  .card-front .brand { color: var(--ink); font-size: 34px; }
  .employee { padding-top: 0; }
  .employee-name { color: var(--red); font-size: 13px; line-height: 16px; }
  .employee-title { font-size: 8px; color: var(--ink); }
  .card-front .company-block { border: 0; padding: 26px 0 0 32px; color: var(--ink); font-size: 8.5px; line-height: 12px; }
  .card-front .contact-list { padding-top: 20px; font-size: 8.5px; line-height: 12.5px; color: var(--ink); }
  .card-front-footer { height: 12px; background: var(--black); border-top: 2px solid var(--red); }
</style>
</head>
<body>

<svg class="icon-defs" aria-hidden="true">
  <symbol id="icon-phone" viewBox="0 0 10 10"><path d="M2 0.5h2l1 2.5-1.3 1a6 6 0 0 0 2.3 2.3l1-1.3 2.5 1v2a1.5 1.5 0 0 1-1.5 1.5A8.5 8.5 0 0 1 0.5 2 1.5 1.5 0 0 1 2 0.5z"/></symbol>
  <symbol id="icon-fax" viewBox="0 0 10 10"><path d="M2.5 0.5h5v2.5h-5z M0.5 3.5h9v4.5h-2v-2h-5v2h-2z M3 6.5h4v3h-4z"/></symbol>
  <symbol id="icon-mail" viewBox="0 0 10 10"><path d="M0.5 2h9v6h-9z M0.5 2l4.5 3.5 4.5-3.5" stroke="#fff" stroke-width="0.8"/></symbol>
  <symbol id="icon-web" viewBox="0 0 10 10"><path d="M5 0.5a4.5 4.5 0 1 0 0.01 0z M5 2a3 3 0 1 1-0.01 0z"/><path d="M1 5h8 M5 1v8" stroke="#e0232b" stroke-width="0.8"/></symbol>
</svg>

<section class="letterhead">
  <header class="letterhead-header">
    <span class="brand">Bramble</span>
    <div class="company-block">
      <div class="company-name">Bramble Logic, LLC</div>
      <div>Address 24 RD 4410</div>
      <div>Millbrook CA 54321 HOLLOW</div>
      <div>Address 24 RD 4410</div>
      <div>Millbrook CA 54321</div>
    </div>
    <ul class="contact-list">
      <li><svg><use href="#icon-phone"/></svg>+ 0 123 456 780</li>
      <li><svg><use href="#icon-fax"/></svg>+ 0 123 456 781</li>
      <li><svg><use href="#icon-mail"/></svg>info@bramblelogicllc.com</li>
      <li><svg><use href="#icon-web"/></svg>www.bramblelogicllc.com</li>
    </ul>
  </header>
  <div class="letter-body">
    <div class="greeting">Dear Client,</div>
    <p>Lorem ipsum dolor sit amet, consectetur adipisicing elit, sed do eiusmod tempor incididunt ut labore et dolore magna aliqua. Ut enim ad minim veniam, quis nostrud exercitation ullamco laboris nisi ut aliquip ex ea commodo consequat. Duis aute irure dolor in reprehenderit in voluptate velit esse cillum dolore eu fugiat nulla pariatur. Excepteur sint occaecat cupidatat non proident, sunt in culpa qui officia deserunt mollit anim id est laborum.</p>
    <p>Lorem ipsum dolor sit amet, consectetur adipisicing elit, sed do eiusmod tempor incididunt ut labore et dolore magna aliqua. Ut enim ad minim veniam, quis nostrud exercitation ullamco laboris nisi ut aliquip ex ea commodo consequat. Duis aute irure dolor in reprehenderit in voluptate velit esse cillum dolore eu fugiat nulla pariatur. Excepteur sint occaecat cupidatat non proident, sunt in culpa qui officia deserunt mollit anim id est laborum.</p>
    <p>Lorem ipsum dolor sit amet, consectetur adipisicing elit, sed do eiusmod tempor incididunt ut labore et dolore magna aliqua. Ut enim ad minim veniam, quis nostrud exercitation ullamco laboris nisi ut aliquip ex ea commodo consequat. Duis aute irure dolor in reprehenderit in voluptate velit esse cillum dolore eu fugiat nulla pariatur. Excepteur sint occaecat cupidatat non proident, sunt in culpa qui officia deserunt mollit anim id est laborum.</p>
    <p>Lorem ipsum dolor sit amet, consectetur adipisicing elit, sed do eiusmod tempor incididunt ut labore et dolore magna aliqua. Ut enim ad minim veniam, quis nostrud exercitation ullamco laboris nisi ut aliquip ex ea commodo consequat. Duis aute irure dolor in reprehenderit in voluptate velit esse cillum dolore eu fugiat nulla pariatur. Excepteur sint occaecat cupidatat non proident, sunt in culpa qui officia deserunt mollit anim id est laborum.</p>
    <p>Lorem ipsum dolor sit amet, consectetur adipisicing elit, sed do eiusmod tempor incididunt ut labore et dolore magna aliqua. Ut enim ad minim veniam, quis nostrud exercitation ullamco laboris nisi ut aliquip ex ea commodo consequat. Duis aute irure dolor in reprehenderit in voluptate velit esse cillum dolore eu fugiat nulla pariatur. Excepteur sint occaecat cupidatat non proident, sunt in culpa qui officia deserunt mollit anim id est laborum.</p>
    <div class="sign-off">Yours Sincerely,</div>
    <div class="signature-row">
      <div class="signature" role="img" aria-label="Handwritten signature of Owen Hale"></div>
      <div class="signer">Owen Hale<br>Executive manager</div>
    </div>
  </div>
  <footer class="letterhead-footer"></footer>
</section>

<section class="card card-back">
  <span class="brand">Bramble</span>
  <span class="card-url">www.bramblelogicllc.com</span>
</section>

<section class="card card-front">
  <div class="card-front-main">
    <span class="brand">Bramble</span>
    <div class="employee">
      <div class="employee-name">Nadia Ferrell</div>
      <div class="employee-title">General Manager</div>
    </div>
    <div class="company-block">
      <div class="company-name">Bramble Logic, LLC</div>
      <div>Address 24 RD 4410</div>
      <div>Millbrook CA 54321 HOLLOW</div>
      <div>Address 24 RD 4410</div>
      <div>Millbrook CA 54321</div>
    </div>
    <ul class="contact-list">
      <li><svg><use href="#icon-phone"/></svg>+ 0 123 456 780</li>
      <li><svg><use href="#icon-fax"/></svg>+ 0 123 456 781</li>
      <li><svg><use href="#icon-mail"/></svg>info@bramblelogicllc.com</li>
      <li><svg><use href="#icon-web"/></svg>www.bramblelogicllc.com</li>
    </ul>
  </div>
  <footer class="card-front-footer"></footer>
</section>

</body>
</html>
```